Small Verses Across the Winter Years

Need a BOOK COVER, SPINE, and BACK for above named book. This is the story of my late wife (a university professor) told through her own songs and poems. It is about the people she loved, especially her grand children, her extensive professional and life interests, her family, friends, and festivities, her illness, etc.
Updates

Target Market(s)

Family and friends

Font styles to use
Other font styles liked:
• Times New Roman

Requirements
Must have
• Regret I haven't given much thought to it...
Nice to have
• Regret I haven't given much thought to it..
Should not have

```html
<!DOCTYPE html>
<html lang="en">
<head>
<meta charset="utf-8">
<title>Small Verses Across the Winter Years — Cover Spread</title>
<link href="https://fonts.googleapis.com/css2?family=Young+Serif&family=Gelasio:ital,wght@0,400;0,500;1,400&display=swap" rel="stylesheet">
<style>
  :root {
    --page-bg: #e4e3df;
    --paper: #ffffff;
    --ink-plum: #3b1a55;
    --ink-amp: #7d5c95;
    --ink-violet: #7b4a9f;
    --ink-spine: #2e1f3a;
    --wash-blue: #b9c8cf;
    --wash-warm: #efe4cf;
  }
  * { box-sizing: border-box; margin: 0; padding: 0; }
  html, body { width: 887px; height: 1200px; overflow: hidden; }
  body { background: var(--page-bg); position: relative; }

  .cover-spread {
    position: absolute; left: 0; top: 272px;
    width: 887px; height: 656px;
    background: var(--paper);
    box-shadow: 0 2px 6px rgba(0,0,0,0.12);
  }

  .title-block { position: absolute; font-family: "Young Serif", serif; color: var(--ink-plum); line-height: 1; }
  .title-block span { position: absolute; white-space: nowrap; }
  .title-block .connector { color: var(--ink-amp); font-family: "Gelasio", serif; font-style: italic; }

  .front-title { left: 512px; top: 30px; width: 370px; height: 270px; }
  .front-title .w1 { left: 0; top: 8px; font-size: 74px; }
  .front-title .w2 { right: 20px; top: 76px; font-size: 74px; }
  .front-title .w3 { left: 10px; top: 158px; font-size: 30px; }
  .front-title .w3 .connector { font-size: 30px; }
  .front-title .w4 { right: 0; top: 198px; font-size: 60px; }

  .back-title { left: 80px; top: 62px; width: 260px; height: 200px; }
  .back-title .w1 { left: 0; top: 4px; font-size: 44px; }
  .back-title .w2 { right: 12px; top: 48px; font-size: 44px; }
  .back-title .w3 { left: 4px; top: 100px; font-size: 18px; }
  .back-title .w4 { right: 0; top: 124px; font-size: 36px; }

  .back-blurb {
    position: absolute; left: 83px; top: 283px; width: 246px;
    font-family: "Gelasio", serif; font-size: 9.6px; line-height: 10.8px;
    color: var(--ink-violet); text-align: justify;
  }
  .back-blurb p + p { margin-top: 10px; }
  .back-blurb p.tight { margin-top: 0; }

  .spine {
    position: absolute; left: 424px; top: 0; width: 40px; height: 656px;
    font-family: "Gelasio", serif; font-size: 15px; color: var(--ink-spine);
  }
  .spine span { position: absolute; left: 10px; writing-mode: vertical-rl; white-space: nowrap; }
  .spine .spine-author { top: 54px; }
  .spine .spine-title { top: 300px; }

  .cover-illustration {
    position: absolute; left: 660px; top: 286px; width: 227px; height: 332px;
    background: radial-gradient(ellipse at 40% 35%, var(--wash-blue) 0%, #d6dde0 45%, var(--wash-warm) 75%, var(--paper) 100%);
    border-radius: 46% 10% 0 30% / 30% 10% 0 20%;
  }

  .front-author {
    position: absolute; left: 576px; top: 622px; width: 240px; text-align: center;
    font-family: "Gelasio", serif; font-size: 16.5px; letter-spacing: 0.3px; color: var(--ink-violet);
  }
</style>
</head>
<body>
  <section class="cover-spread">
    <div class="title-block back-title">
      <span class="w1">Small</span>
      <span class="w2">Verses</span>
      <span class="w3">Across the <span class="connector">Winter</span></span>
      <span class="w4">Years</span>
    </div>

    <div class="back-blurb">
      <p>This collection gathers the songs and poems of a beloved professor and grandmother, written across many seasons of her life. Here are verses for grandchildren and old friends, for festivals and quiet evenings, for lecture halls and kitchen tables, for travel, music, learning and the long patience of illness. Each piece carries her voice, warm and curious, always reaching toward the people she loved.</p>
      <p>Gathered by her husband, these pages are a gift to family and friends who shared her table, her laughter and her songs, and to the grandchildren who will one day read them aloud.</p>
      <p class="tight">May these small verses keep her company in every home where she is remembered, and in every season still to come.</p>
    </div>

    <div class="spine">
      <span class="spine-author">Meera Kalsekar Rao</span>
      <span class="spine-title">Small Verses Across the Winter Years</span>
    </div>

    <div class="title-block front-title">
      <span class="w1">Small</span>
      <span class="w2">Verses</span>
      <span class="w3">Across the <span class="connector">Winter</span></span>
      <span class="w4">Years</span>
    </div>

    <div class="cover-illustration" role="img" aria-label="Watercolour illustration of a grandmother reading a poem aloud to a young granddaughter, with a cat curled at her feet"></div>

    <p class="front-author">Meera Kalsekar Rao</p>
  </section>
</body>
</html>
```